" O aplicativo coleta informações em campo através de pontos georreferenciados com entrada de detalhes(descrições), fotos e áudio. As informações coletadas em campo são exportadas para ser processadas e assim, gerados dados estatísticos em outra plataforma. "

```html
<!DOCTYPE html>
<html lang="pt-BR">
<head>
<meta charset="utf-8">
<title>Levantamentos – Alerta</title>
<link rel="stylesheet" href="https://fonts.googleapis.com/css2?family=Roboto:wght@400;500;700&display=swap">
<style>
  :root {
    --bg: #f2f2f2;
    --status-green: #0b6a4e;
    --header-bg: #eceeed;
    --brand-green: #1f8a4c;
    --alert-green: #33c46c;
    --text-dark: #333a36;
    --text-mid: #6b716d;
    --line: #cfd3d1;
    --screen-bg: #f7f8f7;
    --overlay: rgba(80, 84, 82, 0.55);
    --white: #ffffff;
  }
  * { box-sizing: border-box; margin: 0; padding: 0; }
  html, body { width: 1200px; height: 1200px; overflow: hidden; }
  body { background: var(--bg); font-family: "Roboto", sans-serif; color: var(--text-dark); }

  .app-screen {
    position: absolute; left: 300px; top: 75px; width: 600px; height: 1050px;
    background: var(--screen-bg); overflow: hidden;
    box-shadow: 0 6px 30px rgba(0,0,0,0.12);
  }
  .status-bar {
    height: 45px; background: var(--status-green); color: var(--white);
    display: flex; align-items: center; justify-content: space-between;
    padding: 0 22px; font-size: 19px; font-weight: 500;
  }
  .app-header {
    height: 86px; background: var(--header-bg); display: flex; align-items: center;
    padding: 0 28px 0 40px; border-bottom: 1px solid var(--line);
  }
  .brand-square { width: 46px; height: 46px; background: var(--brand-green); border-radius: 3px; }
  .header-titles { margin-left: 34px; flex: 1; }
  .header-title { font-size: 20px; font-weight: 700; color: var(--brand-green); letter-spacing: .5px; }
  .header-sub { font-size: 14px; color: var(--text-mid); margin-top: 3px; }
  .menu-icon { width: 32px; height: 24px; }

  .section-tab {
    height: 70px; display: flex; align-items: center; padding: 0 28px;
    font-size: 20px; color: var(--brand-green); border-bottom: 1px solid var(--line);
  }
  .point-row {
    height: 56px; display: flex; align-items: center; padding: 0 28px;
    font-size: 15px; color: var(--text-mid); border-bottom: 1px solid var(--line);
  }
  .point-accuracy { margin-left: 50px; color: var(--brand-green); font-weight: 500; }
  .point-tools { margin-left: auto; display: flex; gap: 16px; }
  .point-tools span { width: 20px; height: 20px; border: 2px solid var(--text-mid); border-radius: 3px; }

  .form-area { padding: 22px 50px; }
  .field-label { font-size: 17px; color: var(--text-dark); margin-bottom: 10px; }
  .field-box { height: 140px; border: 1px solid var(--line); background: var(--white); margin-bottom: 30px; }
  .field-line { height: 60px; border: 1px solid var(--line); background: var(--white); margin-bottom: 30px; }
  .action-bar { height: 70px; background: var(--brand-green); width: 200px; margin-top: 60px; }

  .screen-overlay { position: absolute; inset: 131px 0 0 0; background: var(--overlay); }

  .alert-dialog {
    position: absolute; left: 58px; top: 319px; width: 473px; height: 473px;
    background: var(--white); box-shadow: 0 4px 18px rgba(0,0,0,0.25);
  }
  .alert-header {
    height: 86px; background: var(--alert-green); color: var(--white);
    display: flex; align-items: center; justify-content: space-between; padding: 0 26px 0 24px;
  }
  .alert-title { font-size: 22px; font-weight: 500; letter-spacing: 1px; }
  .alert-body { text-align: center; padding-top: 40px; }
  .alert-icon { width: 64px; height: 56px; }
  .alert-message { font-size: 26px; color: var(--text-dark); margin-top: 24px; }
  .alert-question { font-size: 21px; font-weight: 700; color: var(--text-dark); margin-top: 28px; letter-spacing: .5px; }
  .alert-actions { display: flex; justify-content: center; gap: 24px; margin-top: 40px; }
  .alert-button {
    width: 180px; height: 66px; border: 2px solid #9aa09c; background: var(--white);
    color: var(--brand-green); font-family: "Roboto", sans-serif; font-size: 21px; font-weight: 700;
  }
</style>
</head>
<body>
  <main class="app-screen">
    <div class="status-bar"><span>05/10/2017</span><span>00:00</span><span>100%</span></div>
    <header class="app-header">
      <div class="brand-square"></div>
      <div class="header-titles">
        <div class="header-title">LEVANTAMENTOS</div>
        <div class="header-sub">Lado Esquerdo · Escola</div>
      </div>
      <svg class="menu-icon" viewBox="0 0 32 24"><g fill="#555b57"><rect y="1" width="32" height="3"/><rect y="10.5" width="32" height="3"/><rect y="20" width="32" height="3"/></g></svg>
    </header>
    <div class="section-tab">Meio Fio</div>
    <div class="point-row">
      <span>-19,9207150 -43,9906044</span>
      <span class="point-accuracy">8m</span>
      <div class="point-tools"><span></span><span></span><span></span></div>
    </div>
    <section class="form-area">
      <div class="field-label">Descrição Geral</div>
      <div class="field-box"></div>
      <div class="field-line"></div>
      <div class="field-line"></div>
      <div class="action-bar"></div>
    </section>

    <div class="screen-overlay"></div>

    <div class="alert-dialog" role="alertdialog">
      <div class="alert-header">
        <svg width="30" height="26" viewBox="0 0 30 26"><path d="M10 4 L4 10 L10 16 M4 10 H20 Q26 10 26 16 V22" fill="none" stroke="#fff" stroke-width="2.5"/></svg>
        <span class="alert-title">ALERTA</span>
      </div>
      <div class="alert-body">
        <svg class="alert-icon" viewBox="0 0 64 56"><path d="M32 4 L60 52 H4 Z" fill="none" stroke="#1f8a4c" stroke-width="4" stroke-linejoin="round"/><rect x="30" y="20" width="4" height="18" fill="#1f8a4c"/><rect x="30" y="42" width="4" height="4" fill="#1f8a4c"/></svg>
        <p class="alert-message">Este Segmento será fechado.</p>
        <p class="alert-question">DESEJA CONTINUAR?</p>
        <div class="alert-actions">
          <button class="alert-button">SIM</button>
          <button class="alert-button">NÃO</button>
        </div>
      </div>
    </div>
  </main>
</body>
</html>
```